One pager Business Profile BrightHire

We would like to create a onepage with our company profile. It is important to keep the basis like it is in the word document but make it nice and fancy. Consistancy in color and fonts is important.

I've added the logo so you can pick the correct colors. The small logo's you can reuse, I want to replace them once you are ready.

In the word document we used standard Word stuff, I would like nice symbols and a professional well designed block in the Cooperation part

I would like to have a source file so I can change (and translate) text, so better to use a regular font or free font (I need the font than).

Target Market(s)

Recruitment

Industry/Entity Type

Recruitment

Requirements
Must have
• a professional look

```html
<!DOCTYPE html>
<html lang="en">
<head>
<meta charset="utf-8">
<title>BrightHire – Business Profile</title>
<link rel="stylesheet" href="https://fonts.googleapis.com/css2?family=Open+Sans:wght@400;600;700;800&family=Montserrat:wght@500;600&display=swap">
<style>
  :root{
    --blue-dark:#1d5f9e;
    --blue:#2a78bf;
    --blue-light:#49a6dc;
    --cyan:#1aa6d6;
    --navy:#2d3a4f;
    --sky:#5bc3ea;
    --coral:#f07057;
    --slate:#5a87c8;
    --text:#3c3c3c;
    --heading:#2b2f36;
    --white:#ffffff;
  }
  *{box-sizing:border-box;margin:0;padding:0}
  html,body{width:905px;height:1200px;overflow:hidden}
  body{font-family:"Open Sans",Arial,sans-serif;color:var(--text);background:var(--white)}
  .flyer{position:relative;width:905px;height:1200px;background:linear-gradient(180deg,var(--blue) 0%,var(--blue-dark) 100%);overflow:hidden}

  .masthead{position:absolute;left:0;top:0;width:905px;height:130px;background:var(--white);border-top-right-radius:110px}
  .brand{position:absolute;left:36px;top:44px;font-family:"Montserrat",sans-serif;font-weight:600;font-size:36px;letter-spacing:6px;color:#4a4f57}

  .hero{position:absolute;left:0;top:96px;width:905px;height:319px;background:linear-gradient(90deg,var(--blue-dark) 0%,var(--blue) 60%,var(--blue-light) 100%);border-top-right-radius:150px}
  .hero-title{position:absolute;left:36px;top:82px;color:var(--white);font-weight:700;font-size:26px;letter-spacing:1.5px}
  .hero-rule{position:absolute;left:36px;top:124px;width:126px;height:2px;background:var(--white)}
  .hero-sub{position:absolute;left:36px;top:142px;color:var(--white);font-weight:700;font-size:19px}
  .hero-text{position:absolute;left:36px;top:178px;width:372px;color:var(--white);font-size:14px;line-height:19px;text-align:justify}
  .hero-art{position:absolute;left:450px;top:24px;width:360px;height:272px;border-radius:50%;background:radial-gradient(circle,#d8ecf8 0%,#7fc0ea 55%,rgba(73,166,220,0) 72%)}

  .body-panel{position:absolute;left:0;top:415px;width:905px;height:722px;background:var(--white);border-bottom-right-radius:120px}
  .section-title{position:absolute;font-weight:800;font-size:20px;color:var(--heading);letter-spacing:.3px}
  .section-title .accent{color:var(--blue)}
  .offer-title{left:36px;top:20px}
  .offer-text{position:absolute;left:36px;top:52px;width:372px;font-size:14px;line-height:19px;text-align:justify}

  .open-title{left:36px;top:278px}
  .open-item{position:absolute;left:36px;width:380px;display:flex;gap:14px;align-items:flex-start;font-size:14px;line-height:18px}
  .open-item svg{flex:0 0 44px}
  .open-item p{padding-top:4px}

  .teams-title{left:36px;top:497px}
  .teams-list{position:absolute;left:36px;top:530px;list-style:none;font-size:14px;line-height:19.6px}
  .teams-list li::before{content:"•";color:var(--blue);margin-right:8px}

  .years{position:absolute;left:428px;top:28px;width:70px;text-align:center;color:var(--cyan)}
  .years-num{font-size:58px;font-weight:700;line-height:56px}
  .years-label{font-size:12px;font-weight:700;letter-spacing:1px;color:var(--heading)}
  .fact-text{position:absolute;left:520px;width:240px;font-size:14px;line-height:17px}
  .review-icon{position:absolute;left:432px;top:118px}

  .client-cloud{position:absolute;left:430px;top:252px;width:330px;height:150px}
  .client-dot{position:absolute;border-radius:50%}

  .flow-arrow{position:absolute;top:428px;width:12px;height:254px}
  .flow-label{position:absolute;top:555px;font-size:10px;letter-spacing:.5px;color:var(--heading);white-space:nowrap}
  .flow-label.left{left:412px;transform:translate(-50%,-50%) rotate(-90deg)}
  .flow-label.right{left:788px;transform:translate(-50%,-50%) rotate(90deg)}

  .coop-bar{position:absolute;left:448px;width:301px;border-radius:14px;color:var(--white);display:flex;align-items:center;justify-content:center;text-align:center}
  .coop-head{top:418px;height:39px;background:var(--blue-dark);font-weight:700;font-size:16px;letter-spacing:.5px}
  .coop-platform{top:597px;height:38px;background:var(--slate);font-size:15px;letter-spacing:.5px}
  .coop-pool{top:643px;height:36px;background:var(--cyan);font-size:11px;font-weight:700}
  .coop-box{position:absolute;top:467px;height:116px;border-radius:10px;color:var(--white);display:flex;flex-direction:column;align-items:center;justify-content:center;gap:8px;font-size:11px;line-height:13px;text-align:center}
  .box-group{left:448px;width:95px;background:var(--navy)}
  .box-network{left:553px;width:92px;background:var(--sky)}
  .box-client{left:655px;width:94px;background:var(--coral)}

  .footer{position:absolute;left:0;top:1137px;width:905px;height:63px;display:flex;align-items:center;color:var(--white);font-size:12.5px}
  .footer-item{position:absolute;display:flex;align-items:center;gap:7px}
  .footer-item svg{flex:0 0 14px}
</style>
</head>
<body>
<main class="flyer">

  <header class="masthead">
    <div class="brand">BRIGHTHIRE</div>
  </header>

  <section class="hero">
    <h1 class="hero-title">BETTER EXPERTS, FASTER</h1>
    <div class="hero-rule"></div>
    <h2 class="hero-sub">The best developers in our network</h2>
    <p class="hero-text">As part of the Northvale Group and our partner network, BrightHire is able to provide clients with full development teams, complete with test automators, scrum masters, product owners and business analysts and developers..</p>
    <div class="hero-art" role="img" aria-label="Illustration of a team working around a large monitor with gears, a checklist and a magnifying glass"></div>
  </section>

  <section class="body-panel">
    <h3 class="section-title offer-title">OUR <span class="accent">OFFER</span></h3>
    <p class="offer-text">BrightHire helps you solve your IT organisation's capacity problems by offering and deploying high-quality, highly developed candidates. Our candidates, our professionals, are driven, and they are used to getting the best out of themselves and their project. They bring up-to-date knowledge for you, so they immediately tap the best level for you as a client to help achieve the objectives of the project, and therefore really complement your team. Our professionals are of immediate value and deliver demonstrable results..</p>

    <h3 class="section-title open-title">TRANSPARANT <span class="accent">&amp; OPEN</span></h3>
    <div class="open-item" style="top:312px">
      <svg width="44" height="44" viewBox="0 0 44 44" fill="none" stroke="#2b2f36" stroke-width="1.6"><circle cx="11" cy="12" r="4"/><circle cx="33" cy="12" r="4"/><path d="M4 28c0-5 3-8 7-8s7 3 7 8M26 28c0-5 3-8 7-8s7 3 7 8"/><path d="M14 36h16M16 32l-3 4 3 4M28 32l3 4-3 4" stroke="#2a78bf"/></svg>
      <p>BrightHire stands for transparency and openness, for both client and contractor.</p>
    </div>
    <div class="open-item" style="top:370px">
      <svg width="44" height="44" viewBox="0 0 44 44" fill="none" stroke="#2b2f36" stroke-width="1.6"><rect x="8" y="4" width="26" height="34" rx="2"/><path d="M13 12h16M13 18h16M13 24h10" stroke="#2a78bf"/><rect x="24" y="22" width="12" height="16" rx="1" fill="#fff"/><path d="M27 27h6M27 31h6"/></svg>
      <p>Clear agreements and no unnecessary obligations.</p>
    </div>
    <div class="open-item" style="top:428px">
      <svg width="44" height="44" viewBox="0 0 44 44" fill="none" stroke="#2b2f36" stroke-width="1.6"><path d="M6 16a12 12 0 0 1 22-6"/><path d="M28 4v6h-6"/><circle cx="16" cy="18" r="3" stroke="#2a78bf"/><circle cx="30" cy="28" r="8"/><path d="M30 23v5l3 2" stroke="#2a78bf"/></svg>
      <p>Short lines, and smooth response times.<br>For both the client and the professional.</p>
    </div>

    <h3 class="section-title teams-title">EXPERTISESE <span class="accent">TEAMS</span></h3>
    <ul class="teams-list">
      <li>Backend developers</li>
      <li>Frontend developers (web frameworks)</li>
      <li>Platform developers</li>
      <li>Data engineers</li>
      <li>Devops (cloud platforms)</li>
      <li>Server-side developers</li>
      <li>Testers (automation &amp; functioneel)</li>
      <li>Mobile developers (phone / tablet)</li>
      <li>UX/UI developers</li>
    </ul>

    <div class="years">
      <div class="years-num">15</div>
      <div class="years-label">YEARS</div>
    </div>
    <p class="fact-text" style="top:36px">We have access to a specialist network of software development professionals carefully built up over a period of 15 years</p>

    <svg class="review-icon" width="60" height="76" viewBox="0 0 60 76" fill="none" stroke="#2b2f36" stroke-width="2"><rect x="4" y="8" width="40" height="62" rx="3"/><rect x="15" y="3" width="18" height="9" rx="2" fill="#fff"/><circle cx="18" cy="34" r="8"/><path d="M14 34l3 3 5-6" stroke="#2a78bf"/><path d="M38 28l2 4 4 .5-3 3 .8 4-3.8-2-3.8 2 .8-4-3-3 4-.5z M50 28l2 4 4 .5-3 3 .8 4-3.8-2-3.8 2 .8-4-3-3 4-.5z M38 44l2 4 4 .5-3 3 .8 4-3.8-2-3.8 2 .8-4-3-3 4-.5z" fill="#1aa6d6" stroke="none"/><path d="M12 58h14"/></svg>
    <p class="fact-text" style="top:128px">By employing qualitatively suitable candidates, we receive positive customer reviews and score high customer satisfaction.</p>

    <div class="client-cloud" aria-label="Client references">
      <div class="client-dot" style="left:0;top:30px;width:38px;height:38px;background:#f5c400"></div>
      <div class="client-dot" style="left:42px;top:6px;width:44px;height:44px;background:#1f3c8f"></div>
      <div class="client-dot" style="left:60px;top:50px;width:30px;height:30px;background:#1aa6d6"></div>
      <div class="client-dot" style="left:96px;top:2px;width:36px;height:36px;background:#f7a535"></div>
      <div class="client-dot" style="left:100px;top:42px;width:32px;height:32px;background:#e6223b"></div>
      <div class="client-dot" style="left:138px;top:0;width:40px;height:40px;background:#1b2a55"></div>
      <div class="client-dot" style="left:144px;top:48px;width:34px;height:34px;background:#2a78bf"></div>
      <div class="client-dot" style="left:184px;top:4px;width:34px;height:34px;background:#1d4b8f"></div>
      <div class="client-dot" style="left:184px;top:44px;width:26px;height:26px;background:#2d6ab5"></div>
      <div class="client-dot" style="left:222px;top:10px;width:40px;height:40px;background:#173a7a"></div>
      <div class="client-dot" style="left:266px;top:22px;width:40px;height:40px;background:#1b6e4a"></div>
      <div class="client-dot" style="left:226px;top:58px;width:34px;height:34px;background:#f37021"></div>
      <div class="client-dot" style="left:12px;top:76px;width:36px;height:36px;background:#d9d9d9"></div>
      <div class="client-dot" style="left:54px;top:86px;width:30px;height:30px;background:#c42128"></div>
      <div class="client-dot" style="left:92px;top:82px;width:26px;height:26px;background:#111"></div>
      <div class="client-dot" style="left:124px;top:88px;width:38px;height:28px;border-radius:6px;background:#1f2c4f"></div>
      <div class="client-dot" style="left:166px;top:80px;width:28px;height:28px;background:#4a8bd1"></div>
      <div class="client-dot" style="left:198px;top:76px;width:30px;height:30px;background:#7ab648"></div>
      <div class="client-dot" style="left:130px;top:122px;width:64px;height:22px;border-radius:4px;background:#2b2f36"></div>
    </div>

    <svg class="flow-arrow" style="left:426px" viewBox="0 0 12 254" fill="none" stroke="#2a78bf" stroke-width="1.5"><path d="M6 2v250M1 8l5-6 5 6M1 246l5 6 5-6"/></svg>
    <span class="flow-label left">CUSTOMER REQUEST</span>
    <svg class="flow-arrow" style="left:760px" viewBox="0 0 12 254" fill="none" stroke="#2a78bf" stroke-width="1.5"><path d="M6 2v250M1 8l5-6 5 6M1 246l5 6 5-6"/></svg>
    <span class="flow-label right">CUSTOMER REQUEST</span>

    <div class="coop-bar coop-head">COOPERATION</div>
    <div class="coop-box box-group">
      <svg width="30" height="30" viewBox="0 0 30 30" fill="none" stroke="#fff" stroke-width="1.5"><circle cx="15" cy="15" r="13"/><circle cx="15" cy="11" r="3"/><circle cx="8" cy="15" r="2.5"/><circle cx="22" cy="15" r="2.5"/><path d="M10 22c0-3 2-5 5-5s5 2 5 5"/></svg>
      <span>NORTHVALE<br>GROEP</span>
    </div>
    <div class="coop-box box-network">
      <svg width="30" height="30" viewBox="0 0 30 30" fill="none" stroke="#fff" stroke-width="1.5"><rect x="4" y="5" width="22" height="15" rx="2"/><path d="M11 25h8M15 20v5"/><circle cx="10" cy="12" r="2"/><circle cx="20" cy="12" r="2"/><path d="M12 12h6"/></svg>
      <span>NETWERK<br>PARTIJEN</span>
    </div>
    <div class="coop-box box-client">
      <svg width="30" height="30" viewBox="0 0 30 30" fill="none" stroke="#fff" stroke-width="1.5"><circle cx="12" cy="10" r="4"/><path d="M4 25c0-5 3-8 8-8s8 3 8 8"/><circle cx="23" cy="18" r="4"/><path d="M23 16v2l1.5 1"/></svg>
      <span>KLANT</span>
    </div>
    <div class="coop-bar coop-platform">BRIGHTHIRE</div>
    <div class="coop-bar coop-pool">ZZP'ers&nbsp;&nbsp;|&nbsp;DEVELOPERS</div>
  </section>

  <footer class="footer">
    <div class="footer-item" style="left:36px">
      <svg width="14" height="14" viewBox="0 0 14 14"><circle cx="7" cy="7" r="7" fill="#fff" fill-opacity=".35"/><path d="M7 3a2.5 2.5 0 0 0-2.5 2.5C4.5 8 7 11 7 11s2.5-3 2.5-5.5A2.5 2.5 0 0 0 7 3z" fill="#fff"/></svg>
      <span>Kanaalstraat 18 3511 AB&nbsp; Utrecht</span>
    </div>
    <div class="footer-item" style="left:289px">
      <svg width="14" height="14" viewBox="0 0 14 14"><circle cx="7" cy="7" r="7" fill="#fff" fill-opacity=".35"/><path d="M4.5 3.5l1.5-.5 1 2-1 1c.5 1 1.2 1.7 2 2l1-1 2 1-.5 1.5c-3 .3-6.3-3-6-6z" fill="#fff"/></svg>
      <span>0031 30 555 0142</span>
    </div>
    <div class="footer-item" style="left:448px">
      <svg width="14" height="14" viewBox="0 0 14 14" fill="none" stroke="#fff" stroke-width="1"><circle cx="7" cy="7" r="6"/><ellipse cx="7" cy="7" rx="2.5" ry="6"/><path d="M1 7h12"/></svg>
      <span>www.brighthire.example</span>
    </div>
    <div class="footer-item" style="left:623px">
      <svg width="14" height="14" viewBox="0 0 14 14" fill="none" stroke="#fff" stroke-width="1"><circle cx="7" cy="7" r="6.5" fill="#fff" fill-opacity=".35" stroke="none"/><rect x="3" y="4.5" width="8" height="5.5" rx=".8"/><path d="M3 5l4 3 4-3"/></svg>
      <span>info@brighthire.example</span>
    </div>
  </footer>

</main>
</body>
</html>
```